International Legal Service Company needs Letterhead Design

Put my new Logo into Letterhead Design, using updated telephone number, e-mail address and website. Current letterhead and updated information which i want you to include my new letterhead attached herewith. Of course, my new Logo attached herein. Also, you can use slogan "Total Legal Outsourcing Solutions For Multinational Businesses"

It Company

```html
<!DOCTYPE html>
<html lang="en">
<head>
<meta charset="utf-8">
<title>Harborline Counsel Group Inc — Letterhead</title>
<link rel="stylesheet" href="https://fonts.googleapis.com/css2?family=Noto+Sans:wght@400;700&display=swap">
<style>
  :root {
    --backdrop: #d9d9d9;
    --paper: #ffffff;
    --brand-blue: #0328a8;
    --rule-gray: #555555;
    --text-dark: #2b2b2b;
    --divider: #6a6a6a;
  }
  * { margin: 0; padding: 0; box-sizing: border-box; }
  html, body {
    width: 1001px;
    height: 1200px;
    overflow: hidden;
    background: var(--backdrop);
    font-family: "Noto Sans", Verdana, sans-serif;
  }
  .letterhead {
    position: absolute;
    left: 84px;
    top: 52px;
    width: 834px;
    height: 1079px;
    background: var(--paper);
    overflow: hidden;
  }
  .side-band {
    position: absolute;
    left: 0;
    top: 0;
    width: 73px;
    height: 100%;
    background: var(--brand-blue);
  }
  .side-rule {
    position: absolute;
    left: 83px;
    top: 0;
    width: 6px;
    height: 100%;
    background: var(--rule-gray);
  }
  .brand-disc {
    position: absolute;
    left: 4px;
    top: 19px;
    width: 124px;
    height: 124px;
    border-radius: 50%;
    background: var(--paper);
  }
  .brand-mark {
    position: absolute;
    left: 25px;
    top: 41px;
    width: 80px;
    height: 80px;
    border-radius: 50%;
    background: var(--brand-blue);
  }
  .brand-name {
    position: absolute;
    left: 122px;
    top: 62px;
    color: var(--brand-blue);
    font-weight: 700;
    font-size: 21px;
    line-height: 25px;
    letter-spacing: -0.3px;
  }
  .contact-block {
    position: absolute;
    left: 565px;
    top: 20px;
    padding-left: 11px;
    border-left: 1px solid var(--divider);
    color: var(--text-dark);
    font-size: 14.5px;
    line-height: 19px;
  }
  .contact-address { margin-bottom: 9px; }
  .contact-list { list-style: none; }
  .contact-list li {
    display: flex;
    align-items: center;
    gap: 8px;
    height: 19px;
  }
  .contact-list svg {
    width: 16px;
    height: 16px;
    flex: none;
    fill: var(--text-dark);
  }
  .slogan {
    position: absolute;
    left: 99px;
    bottom: 10px;
    color: #111111;
    font-size: 14.5px;
  }
</style>
</head>
<body>
  <main class="letterhead">
    <div class="side-band"></div>
    <div class="side-rule"></div>
    <div class="brand-disc"></div>
    <div class="brand-mark" aria-hidden="true"></div>
    <div class="brand-name">Harborline Counsel<br>Group Inc</div>

    <address class="contact-block" style="font-style:normal">
      <div class="contact-address">4180 Meadowgate Avenue<br>Suite 310, Fairbrook, MD 20912</div>
      <ul class="contact-list">
        <li>
          <svg viewBox="0 0 16 16" aria-label="Phone"><path d="M8 1a7 7 0 1 0 0 14A7 7 0 0 0 8 1zm0 1.6a5.4 5.4 0 1 1 0 10.8A5.4 5.4 0 0 1 8 2.6zM6 4.2l1.3 1.9-.8.9c.5 1.1 1.3 2 2.4 2.6l.9-.8 1.9 1.3-.9 1.5C8.2 11.3 4.9 8 4.6 5z"/></svg>
          <span>301-555-0147</span>
        </li>
        <li>
          <svg viewBox="0 0 16 16" aria-label="Fax"><path d="M4 1h6l2 2v4H4zM1 8h14v5h-2v-2H3v2H1zM3 12h10v3H3z"/></svg>
          <span>301-555-0183</span>
        </li>
        <li>
          <svg viewBox="0 0 16 16" aria-label="Email"><path d="M1 3h14v1.2L8 8.6 1 4.2zM1 5.8l7 4.4 7-4.4V13H1z"/></svg>
          <span>office@harborlinecounsel.com</span>
        </li>
        <li>
          <svg viewBox="0 0 16 16" aria-label="Website"><path d="M8 1a7 7 0 1 0 0 14A7 7 0 0 0 8 1zm-.7 1.6v2.7H5.1c.5-1.4 1.3-2.4 2.2-2.7zm1.4 0c.9.3 1.7 1.3 2.2 2.7H8.7zM4.8 3.4c-.3.6-.6 1.2-.8 1.9H2.9c.5-.8 1.1-1.4 1.9-1.9zm6.4 0c.8.5 1.4 1.1 1.9 1.9H12c-.2-.7-.5-1.3-.8-1.9zM2.4 6.6h1.3c-.1.5-.1 1-.1 1.4s0 .9.1 1.4H2.4a5.6 5.6 0 0 1 0-2.8zm2.7 0h2.2v2.8H5.1C5 8.9 5 8.5 5 8s0-.9.1-1.4zm3.6 0h2.2c.1.5.1.9.1 1.4s0 .9-.1 1.4H8.7zm3.6 0h1.3a5.6 5.6 0 0 1 0 2.8h-1.3c.1-.5.1-1 .1-1.4s0-.9-.1-1.4zM2.9 10.7H4c.2.7.5 1.3.8 1.9-.8-.5-1.4-1.1-1.9-1.9zm2.2 0h2.2v2.7c-.9-.3-1.7-1.3-2.2-2.7zm3.6 0h2.2c-.5 1.4-1.3 2.4-2.2 2.7zm3.3 0h1.1c-.5.8-1.1 1.4-1.9 1.9.3-.6.6-1.2.8-1.9z"/></svg>
          <span>www.harborlinecounsel.com</span>
        </li>
      </ul>
    </address>

    <p class="slogan">Total Legal Outsourcing Solutions For Multinational Businesses</p>
  </main>
</body>
</html>
```